PTA Meeting Poster

We are looking to create a poster to invite parents of our school to our monthly PTA Meeting.

The copy should include:

PTA Meeting
This Wednesday
8:40am
in the Multi Purpose Room

All Welcome!

```html
<!DOCTYPE html>
<html lang="en">
<head>
<meta charset="UTF-8">
<title>PTA Meeting Poster</title>
<link href="https://fonts.googleapis.com/css2?family=Oswald:wght@600&family=Hind:wght@400;600&display=swap" rel="stylesheet">
<style>
  :root {
    --page-bg: #e9e9e7;
    --board-dark: #0b0b0b;
    --board-mid: #2a2a2a;
    --chalk: #f4f4f4;
    --chalk-soft: #d6d6d6;
    --title-fill: #8a8a8a;
    --desk-light: #d9d9d9;
    --desk-dark: #8c8c8c;
  }
  * { margin: 0; padding: 0; box-sizing: border-box; }
  html, body {
    width: 1200px;
    height: 982px;
    overflow: hidden;
    background: var(--page-bg);
  }
  .poster {
    position: absolute;
    left: 310px;
    top: 46px;
    width: 580px;
    height: 890px;
    background: radial-gradient(ellipse 70% 55% at 50% 42%, var(--board-mid) 0%, var(--board-dark) 75%);
    overflow: hidden;
    box-shadow: 0 6px 20px rgba(0,0,0,0.25);
    font-family: "Hind", sans-serif;
    color: var(--chalk);
    text-align: center;
  }
  .poster__title {
    position: absolute;
    top: 150px;
    left: 0;
    width: 100%;
    font-family: "Oswald", sans-serif;
    font-weight: 600;
    font-size: 82px;
    letter-spacing: -2px;
    color: var(--title-fill);
    -webkit-text-stroke: 3px var(--chalk);
    transform: scaleY(1.12);
  }
  .poster__rule {
    position: absolute;
    left: 145px;
    width: 290px;
    height: 3px;
    background: var(--chalk);
  }
  .poster__rule--top { top: 318px; }
  .poster__rule--bottom { top: 608px; }
  .details {
    position: absolute;
    top: 338px;
    left: 0;
    width: 100%;
    line-height: 1.15;
  }
  .details__day { font-size: 40px; }
  .details__time { font-size: 60px; font-weight: 600; line-height: 1.05; }
  .details__place { font-size: 30px; margin-top: 6px; }
  .welcome {
    position: absolute;
    top: 628px;
    left: 240px;
    width: 300px;
    font-size: 48px;
    line-height: 1.45;
    color: var(--chalk-soft);
    text-align: left;
  }
  .welcome span { display: block; }
  .welcome span:first-child { padding-left: 50px; }
  .desk {
    position: absolute;
    left: 0;
    bottom: 0;
    width: 100%;
    height: 80px;
    background: linear-gradient(180deg, var(--desk-light) 0%, var(--desk-dark) 100%);
  }
  .still-life {
    position: absolute;
    left: 20px;
    bottom: 20px;
    width: 200px;
    height: 200px;
    border-radius: 6px;
    background: linear-gradient(180deg, #7d7d7d 0%, #4a4a4a 55%, #9a9a9a 100%);
  }
</style>
</head>
<body>
  <main class="poster">
    <h1 class="poster__title">PTA MEETING</h1>
    <div class="poster__rule poster__rule--top"></div>
    <div class="details">
      <p class="details__day">THIS WEDNESDAY</p>
      <p class="details__time">8:40AM</p>
      <p class="details__place">IN THE<br>MULTI PURPOSE<br>ROOM</p>
    </div>
    <div class="poster__rule poster__rule--bottom"></div>
    <p class="welcome"><span>ALL</span><span>WELCOME!</span></p>
    <div class="desk"></div>
    <div class="still-life" role="img" aria-label="Apple resting on a stack of books with chalk on a desk"></div>
  </main>
</body>
</html>
```